Four in One (Flexible infographic for Content Management Industry)

See attachment.
A graphic depicting 4 products, where each can stand on its own and each can be combined with others, but where, if all are taken together, the best result is achieved (the "super product").
Intended use is web. See attached file as an example.
The most basic idea is as the attached diagram shows, where 4 rectangles are arranged in a quadrangle, with a middle rectangle in the center representing the combined 4 products. This concept is fine except it is a bit too obvious as it stands. We are looking for either a variation of this or another concept.
The audience is technical + professional + enterprise - NOT consumers. Hence the design should be conservative in nature.
We are aware of tools like as Canva or Pictogram where such graphics are available, but we are looking for something with a bit more imagination and flexibility.
This graphic should be targeted to web sites and be delivered with vector-based (SVG) graphics.

```html
<!DOCTYPE html>
<html lang="en">
<head>
<meta charset="utf-8">
<title>Four in One – Content Management Suite</title>
<link href="https://fonts.googleapis.com/css2?family=Bebas+Neue&family=Roboto:wght@400&display=swap" rel="stylesheet">
<style>
  :root {
    --ink: #111111;
    --body: #3a3a3a;
    --rule: #a8a8a8;
    --lime: #9be800;
    --green: #00d672;
    --cyan: #00e0e6;
    --blue: #00a0da;
    --erp-accent: #00d672;
    --dt-accent: #0096d6;
    --dm-accent: #9be800;
    --sec-accent: #00d8e0;
    --band-start: #008a3e;
    --band-mid: #00928a;
    --band-end: #0577a6;
    --paper: #ffffff;
  }
  * { margin: 0; padding: 0; box-sizing: border-box; }
  html, body { width: 1200px; height: 653px; overflow: hidden; background: var(--paper); }
  .canvas { position: relative; width: 1200px; height: 653px; overflow: hidden; }
  .backdrop { position: absolute; left: 0; top: 0; width: 1200px; height: 652px; }

  .product { position: absolute; font-family: "Roboto", Arial, sans-serif; color: var(--body); }
  .product-title {
    font-family: "Bebas Neue", "Oswald", sans-serif;
    font-weight: 400;
    font-size: 43px;
    line-height: 37px;
    text-align: center;
    color: var(--ink);
    letter-spacing: 0.2px;
  }
  .product-title span { display: block; }
  .erp .product-title .accent { color: var(--erp-accent); }
  .dt .product-title .accent { color: var(--dt-accent); }
  .dm .product-title .accent { color: var(--dm-accent); }
  .sec .product-title .accent { color: var(--sec-accent); }

  .product-summary {
    position: absolute;
    font-size: 13.2px;
    line-height: 16.5px;
    color: var(--body);
    white-space: nowrap;
  }
  .feature-list {
    position: absolute;
    list-style: none;
    display: flex;
    flex-direction: column;
    align-items: center;
  }
  .feature-list li {
    display: flex;
    justify-content: center;
    white-space: nowrap;
    font-size: 13.2px;
    line-height: 16px;
    height: 23.2px;
    padding-top: 1px;
    border-bottom: 1px solid var(--rule);
    color: var(--body);
  }

  /* Enterprise Resource Planning */
  .erp { left: 300px; top: 90px; width: 334px; }
  .erp .product-summary { left: 33px; top: 76px; }
  .erp .feature-list { left: 0; top: 138px; width: 334px; }
  .erp li:nth-child(1) { width: 246px; }
  .erp li:nth-child(2) { width: 223px; }
  .erp li:nth-child(3) { width: 187px; }
  .erp li:nth-child(4) { width: 136px; }

  /* Digital Transformation */
  .dt { left: 860px; top: 90px; width: 302px; }
  .dt .product-summary { left: 12px; top: 78px; }
  .dt .feature-list { left: 0; top: 138px; width: 302px; }
  .dt li:nth-child(1) { width: 246px; }
  .dt li:nth-child(2) { width: 223px; }
  .dt li:nth-child(3) { width: 187px; }
  .dt li:nth-child(4) { width: 136px; }

  /* Document Management */
  .dm { left: 50px; top: 345px; width: 290px; }
  .dm .product-summary { left: 9px; top: 84px; }
  .dm .feature-list { left: 0; top: 145px; width: 290px; }
  .dm li { width: 246px; }

  /* Security and Compliance */
  .sec { left: 590px; top: 345px; width: 298px; }
  .sec .product-summary { left: 5px; top: 84px; }
  .sec .feature-list { left: 0; top: 145px; width: 298px; }
  .sec li { width: 246px; }
</style>
</head>
<body>
<main class="canvas">
  <svg class="backdrop" viewBox="0 0 2560 1390" preserveAspectRatio="none" aria-hidden="true">
    <defs>
      <linearGradient id="band-gradient" x1="0" y1="0" x2="1" y2="0">
        <stop offset="0" stop-color="var(--band-start)"/>
        <stop offset="0.5" stop-color="var(--band-mid)"/>
        <stop offset="1" stop-color="var(--band-end)"/>
      </linearGradient>
    </defs>
    <rect class="connector-band" x="420" y="410" width="1735" height="580" fill="url(#band-gradient)"/>
    <circle class="connector-cutout" cx="995" cy="405" r="347" fill="#ffffff"/>
    <circle class="connector-cutout" cx="415" cy="990" r="345" fill="#ffffff"/>
    <circle class="connector-cutout" cx="1575" cy="995" r="345" fill="#ffffff"/>
    <circle class="connector-cutout" cx="2155" cy="410" r="345" fill="#ffffff"/>
  </svg>

  <svg class="backdrop" viewBox="0 0 2560 1390" preserveAspectRatio="none">
    <rect class="tile tile-dm" x="175" y="168" width="478" height="477" rx="100" fill="var(--lime)" role="img" aria-label="Document management icon: file browser window with folders and a gear"/>
    <rect class="tile tile-sec" x="1338" y="172" width="477" height="476" rx="100" fill="var(--cyan)" role="img" aria-label="Security icon: documents and folder protected by a shield with a padlock"/>
    <rect class="tile tile-erp" x="757" y="753" width="477" height="477" rx="100" fill="var(--green)" role="img" aria-label="Enterprise icon: office building with growth arrow, finance, chart and people badges"/>
    <rect class="tile tile-dt" x="1916" y="755" width="477" height="477" rx="100" fill="var(--blue)" role="img" aria-label="Digital transformation icon: monitor showing a bar chart with circuit connections"/>
  </svg>

  <section class="product erp">
    <h2 class="product-title"><span>Enterprise</span><span class="accent">Resource Planning</span></h2>
    <p class="product-summary">Simplify management across finance, sales,<br>and operations, enabling better decision-<br>making and improved productivity.</p>
    <ul class="feature-list">
      <li>Integrated Business Processes</li>
      <li>Enhanced Decision-Making</li>
      <li>Productivity Improvement</li>
      <li>Check 4</li>
    </ul>
  </section>

  <section class="product dt">
    <h2 class="product-title"><span>Digitital</span><span class="accent">Transformation</span></h2>
    <p class="product-summary">Turn scanned documents into easily<br>searchable digitalarchives, boosting efficiency<br>and accessibility.</p>
    <ul class="feature-list">
      <li>Instant searchable Archives with OCR</li>
      <li>Automated Document Classification</li>
      <li>TeamVault and Cloud Bloh Readv</li>
      <li>Check 4</li>
    </ul>
  </section>

  <section class="product dm">
    <h2 class="product-title"><span>Document</span><span class="accent">Management</span></h2>
    <p class="product-summary">Streamline document organization, access,<br>andcollaboration with easier file storage and<br>sharing, leading to more efficient workflows.</p>
    <ul class="feature-list">
      <li>Centralized Document Control</li>
      <li>Collaborative Workspace Integration</li>
      <li>Automated Compliance Tracking</li>
      <li>Check 4</li>
    </ul>
  </section>

  <section class="product sec">
    <h2 class="product-title"><span>Security</span><span class="accent">and Compliance</span></h2>
    <p class="product-summary">Benefit from tailored cloud solutions, secure<br>data storage,and expert disaster recovery<br>planning for reliable and scalable IT operations.</p>
    <ul class="feature-list">
      <li>Centralized Document Control</li>
      <li>Collaborative Workspace Integration</li>
      <li>Automated Compliance Tracking</li>
      <li>Check 4</li>
    </ul>
  </section>
</main>
</body>
</html>
```